Owen Tasker Studios Business Card

Looking for a clear, modern, elegant, sharp business card that conveys a professional yet edgy image to my business as a wedding, portrait, and travel photographer. Would like something that looks vintage yet modern. Need a new business card to grow my business. We are growing the business for Wedding and Event Photography as well as fine art Photography. (Mostly Landscapes)
Updates

I’m looking through designs now but I have a new logo that i want using please.

New logo uploaded please redesign using that

PLEASE ALL DESIGNERS LOOK IN BRIEF FOR NEW LOGO

Target Market(s)

Brides, Grooms, Families with Kids, People looking for Fine Art Photography Artwork

Industry/Entity Type

Photographer

Contact Information for Business Card

Unsure

Font styles to use
Serif

Colors

Designer to choose colors to be used in the design.

Requirements
Must have
• My Website:
• http://taskerlens.examplefolio.net
• Phone:
• 323-481-5206
• Email:
• owentaskerlens@mailbox-example.net
Nice to have
• Would like a sort of shine on the printing finish.
• I like black I think it looks good on a business card.
• Can try working with my logo (png that I've attached)

```html
<!DOCTYPE html>
<html lang="en">
<head>
<meta charset="utf-8">
<title>Owen Tasker Studios Business Card</title>
<link rel="stylesheet" href="https://fonts.googleapis.com/css2?family=Raleway:wght@300&family=Roboto+Slab:wght@600&family=Roboto:wght@300;500&display=swap">
<style>
  :root {
    --page: #e0e0e0;
    --card-light: #f1efe0;
    --card-dark: #333333;
    --ink: #2a2a2a;
    --ink-soft: #444444;
    --paper-text: #f4f4f4;
  }
  * { margin: 0; padding: 0; box-sizing: border-box; }
  html, body { width: 1200px; height: 897px; overflow: hidden; }
  body { background: var(--page); position: relative; font-family: "Roboto", sans-serif; }

  .card { position: absolute; left: 303px; width: 595px; height: 338px; overflow: hidden; }
  .card--front { top: 92px; background: var(--card-light); color: var(--ink); }
  .card--back { top: 469px; background: var(--card-dark); color: var(--paper-text); }

  .line { position: absolute; left: 0; width: 100%; text-align: center; white-space: nowrap; }

  .brand-mark { position: absolute; left: 50%; transform: translateX(-50%); }

  .brand-name {
    font-family: "Raleway", sans-serif; font-weight: 300;
    font-size: 28px; line-height: 34px; letter-spacing: 0.3px;
  }
  .brand-sub {
    font-family: "Raleway", sans-serif; font-weight: 300;
    font-size: 12px; line-height: 14px; letter-spacing: 0.6em; padding-left: 0.6em;
  }

  .person-name {
    font-family: "Roboto Slab", serif; font-weight: 600;
    font-size: 18px; line-height: 22px; letter-spacing: 1.5px;
  }
  .person-role { font-weight: 300; font-size: 14px; line-height: 18px; color: var(--ink-soft); }
  .divider { position: absolute; left: 252px; top: 256px; width: 90px; height: 1px; background: var(--ink-soft); }
  .contact { font-weight: 300; font-size: 14px; line-height: 18px; color: var(--ink-soft); }
  .contact b { font-weight: 500; color: var(--ink); }

  .back-url { font-weight: 300; font-size: 15px; line-height: 20px; letter-spacing: 1.2px; }
</style>
</head>
<body>
  <section class="card card--front" aria-label="Card front">
    <svg class="brand-mark" style="top:42px;width:58px;height:58px" viewBox="0 0 58 58" aria-hidden="true">
      <rect x="0.5" y="0.5" width="57" height="57" fill="none" stroke="var(--ink)" stroke-width="1"/>
    </svg>
    <div class="line brand-name" style="top:111px">OWEN TASKER</div>
    <div class="line brand-sub" style="top:151px">STUDIOS</div>

    <div class="line person-name" style="top:205px">OWEN TASKER</div>
    <div class="line person-role" style="top:229px">Photographer</div>
    <div class="divider"></div>
    <div class="line contact" style="top:264px"><b>P :</b> 323-481-5206 | <b>E :</b> owentaskerlens@mailbox-example.net</div>
    <div class="line contact" style="top:284px"><b>W :</b> http://taskerlens.examplefolio.net</div>
  </section>

  <section class="card card--back" aria-label="Card back">
    <svg class="brand-mark" style="top:106px;width:60px;height:60px" viewBox="0 0 60 60" aria-hidden="true">
      <rect x="0.5" y="0.5" width="59" height="59" fill="none" stroke="var(--paper-text)" stroke-width="1"/>
    </svg>
    <div class="line brand-name" style="top:180px">OWEN TASKER</div>
    <div class="line brand-sub" style="top:220px">STUDIOS</div>
    <div class="line back-url" style="top:298px">taskerlens.examplefolio.net</div>
  </section>
</body>
</html>
```